Lumora Activewear business card design

I need a business card designed for my activewear business. I would like to use the colours pink, purple white and blue. please see attached logo. please include (name) Harriet Welloby (phone) 0417582064 (email) hattieslumora@mailvento.com (ABN) 48715290637 . please include - Free shipping on all orders over $100

Target Market(s)

female

Contact Information for Business Card

Colors

Requirements
Must have
• I need a business card designed for my activewear business. I would like to use the colours pink, purple white and blue. please see attached logo. please include (name) Harriet Welloby (phone) 0417582064 (email) hattieslumora@mailvento.com (ABN) 48715290637 . please include - Free shipping on all orders over $100

```html
<!DOCTYPE html>
<html lang="en">
<head>
<meta charset="utf-8">
<title>Lumora Activewear – Business Card</title>
<link href="https://fonts.googleapis.com/css2?family=Lato:wght@400;700;900&display=swap" rel="stylesheet">
<style>
  :root {
    --backdrop: #3a3a3a;
    --purple: #9c1aac;
    --purple-deep: #8a1a9a;
    --pink-arc: #c57ba3;
    --white: #ffffff;
  }
  html, body {
    margin: 0;
    padding: 0;
    overflow: hidden;
  }
  body {
    width: 1200px;
    height: 912px;
    background: var(--backdrop);
    position: relative;
    font-family: "Lato", sans-serif;
  }
  .card {
    position: absolute;
    width: 560px;
    height: 320px;
    box-shadow: 0 10px 28px rgba(0,0,0,0.45);
    overflow: hidden;
  }
  /* Front side */
  .card-front {
    left: 70px;
    top: 90px;
    background: var(--purple);
    color: var(--white);
  }
  .brand {
    position: absolute;
    display: flex;
    align-items: center;
    gap: 16px;
    font-weight: 900;
    letter-spacing: 1px;
    text-transform: uppercase;
  }
  .brand-mark {
    width: 38px;
    height: 38px;
    border-radius: 50%;
  }
  .card-front .brand {
    left: 110px;
    top: 100px;
    font-size: 64px;
  }
  .card-front .brand-mark { background: var(--white); }
  .shipping-note {
    position: absolute;
    left: 0;
    right: 0;
    bottom: 54px;
    text-align: center;
    font-size: 17px;
    letter-spacing: 0.5px;
    text-transform: uppercase;
  }
  /* Back side */
  .card-back {
    left: 570px;
    top: 500px;
    background: var(--white);
  }
  .card-back svg.sweep {
    position: absolute;
    inset: 0;
  }
  .card-back .brand {
    left: 40px;
    top: 92px;
    font-size: 54px;
    color: var(--purple-deep);
  }
  .card-back .brand-mark {
    width: 32px;
    height: 32px;
    background: var(--purple-deep);
  }
  .contact {
    position: absolute;
    right: 26px;
    top: 196px;
    text-align: right;
    color: var(--white);
  }
  .contact-name {
    font-size: 22px;
    font-weight: 700;
    margin: 0 0 6px;
  }
  .contact-line {
    display: flex;
    justify-content: flex-end;
    align-items: center;
    gap: 7px;
    font-size: 13px;
    margin: 3px 0;
  }
  .contact-line svg { width: 12px; height: 12px; fill: var(--white); }
  .abn {
    position: absolute;
    left: 40px;
    bottom: 16px;
    font-size: 15px;
    color: var(--white);
  }
</style>
</head>
<body>

  <section class="card card-front" aria-label="Card front">
    <div class="brand"><span class="brand-mark"></span><span>Lumora</span></div>
    <p class="shipping-note">Free shipping on all orders over $100</p>
  </section>

  <section class="card card-back" aria-label="Card back">
    <svg class="sweep" viewBox="0 0 560 320" width="560" height="320" aria-hidden="true">
      <path d="M468 0 Q440 250 0 272 L0 320 L560 320 L560 0 Z" fill="var(--purple)"/>
      <path d="M486 0 Q478 120 390 210" fill="none" stroke="var(--pink-arc)" stroke-width="6" stroke-linecap="round"/>
    </svg>

    <div class="brand"><span class="brand-mark"></span><span>Lumora</span></div>

    <div class="contact">
      <p class="contact-name">Harriet Welloby</p>
      <p class="contact-line">0417582064
        <svg viewBox="0 0 24 24" aria-hidden="true"><path d="M6.6 10.8a15.1 15.1 0 0 0 6.6 6.6l2.2-2.2a1 1 0 0 1 1-.25 11.4 11.4 0 0 0 3.6.57 1 1 0 0 1 1 1V20a1 1 0 0 1-1 1A17 17 0 0 1 3 4a1 1 0 0 1 1-1h3.5a1 1 0 0 1 1 1c0 1.25.2 2.45.57 3.57a1 1 0 0 1-.25 1z"/></svg>
      </p>
      <p class="contact-line">hattieslumora@mailvento.com
        <svg viewBox="0 0 24 24" aria-hidden="true"><path d="M2 5h20v14H2z M3 6l9 7 9-7" fill="var(--white)" stroke="var(--purple)" stroke-width="1.5"/></svg>
      </p>
    </div>

    <p class="abn">(ABN) 48715290637</p>
  </section>

</body>
</html>
```